Veterinary Business cards

Redesign Business Card

Information needed on Card:
Hours: Mon-Fri: 4pm -10PM; Sat- Sun- 10 AM- 5PM
Help@tandrelyns.com
www.tandrelyns.com
405-718-2954
4170 SW 38th Ave. okc, ok 73119
*No appointment necessary*

Optional:
Our tag line is "We're here when you need us" - If it fits on the cards.

```html
<!DOCTYPE html>
<html lang="en">
<head>
<meta charset="utf-8">
<title>Tandrelyn's Urgent Care – Business Card</title>
<link rel="stylesheet" href="https://fonts.googleapis.com/css2?family=Roboto:wght@400;500&family=Roboto+Condensed:wght@700&family=Marcellus&family=Kalam&display=swap">
<style>
  :root {
    --backdrop: #2b2b2c;
    --orange: #c47a22;
    --bronze: #7a4b1f;
    --slate: #4a4a4c;
    --navy: #1c355c;
    --paper: #f3f3f3;
    --white: #f4f4f4;
    --ink: #1c355c;
  }
  html, body {
    margin: 0;
    padding: 0;
    width: 1200px;
    height: 1138px;
    overflow: hidden;
    background: var(--backdrop);
  }
  .canvas {
    position: relative;
    width: 1200px;
    height: 1138px;
  }
  .card {
    position: absolute;
    width: 620px;
    height: 375px;
    border-radius: 14px;
    overflow: hidden;
  }

  /* Front */
  .card-front {
    left: 274px;
    top: 186px;
    background: linear-gradient(100deg, var(--bronze) 0%, #6a4725 30%, var(--slate) 58%, var(--navy) 92%);
  }
  .front-brand {
    position: absolute;
    left: 0;
    right: 0;
    top: 92px;
    text-align: center;
    font-family: "Marcellus", serif;
    font-weight: 400;
    color: var(--white);
  }
  .front-brand .brand-name {
    display: block;
    font-size: 60px;
    line-height: 1;
    letter-spacing: 1px;
  }
  .front-brand .brand-sub {
    display: block;
    margin-top: 10px;
    font-size: 22px;
    letter-spacing: 3px;
  }
  .notice-band {
    position: absolute;
    left: 0;
    right: 0;
    top: 279px;
    height: 34px;
    background: linear-gradient(90deg, var(--navy) 0%, #3b4658 35%, #6b5a40 62%, var(--orange) 85%);
    display: flex;
    align-items: center;
    justify-content: center;
    font-family: "Roboto", sans-serif;
    font-size: 15px;
    color: var(--white);
    letter-spacing: 0.3px;
  }
  .hours {
    position: absolute;
    left: 0;
    right: 0;
    top: 326px;
    text-align: center;
    font-family: "Roboto", sans-serif;
    font-size: 16px;
    color: #e6e2dd;
    word-spacing: 1px;
  }

  /* Back */
  .card-back {
    left: 276px;
    top: 608px;
    background: var(--paper);
  }
  .back-brand {
    position: absolute;
    left: 36px;
    top: 150px;
    width: 260px;
    text-align: center;
    font-family: "Marcellus", serif;
    font-weight: 400;
    color: var(--ink);
  }
  .back-brand .brand-name {
    display: block;
    font-size: 36px;
    line-height: 1;
  }
  .back-brand .brand-sub {
    display: block;
    margin-top: 8px;
    font-size: 15px;
    letter-spacing: 2px;
  }
  .contact {
    position: absolute;
    left: 340px;
    top: 90px;
    font-family: "Roboto", sans-serif;
    color: var(--ink);
  }
  .contact .person {
    font-family: "Roboto Condensed", sans-serif;
    font-weight: 700;
    font-size: 24px;
    color: var(--orange);
    margin: 0 0 22px;
  }
  .contact ul {
    list-style: none;
    margin: 0;
    padding: 0;
  }
  .contact li {
    display: flex;
    align-items: center;
    height: 24px;
    font-size: 16.5px;
  }
  .contact li svg {
    width: 14px;
    height: 14px;
    margin-right: 13px;
    fill: var(--orange);
  }
  .contact .address {
    margin-top: 6px;
    font-size: 16.5px;
  }
  .back-footer {
    position: absolute;
    left: 0;
    bottom: 0;
    width: 620px;
    height: 48px;
  }
  .tagline {
    position: absolute;
    right: 40px;
    bottom: 8px;
    font-family: "Kalam", cursive;
    font-size: 18px;
    color: var(--white);
  }
</style>
</head>
<body>
<main class="canvas">

  <section class="card card-front" aria-label="Card front">
    <div class="front-brand">
      <span class="brand-name">Tandrelyn's</span>
      <span class="brand-sub">URGENT CARE</span>
    </div>
    <div class="notice-band">NO APPOINTMENT NECESSARY</div>
    <p class="hours" style="margin:0">Hours: Mon-Fri: 4PM -10PM &nbsp;|&nbsp; Sat-Sun- 10AM- 5PM</p>
  </section>

  <section class="card card-back" aria-label="Card back">
    <div class="back-brand">
      <span class="brand-name">Tandrelyn's</span>
      <span class="brand-sub">URGENT CARE</span>
    </div>

    <div class="contact">
      <p class="person">Dr. Maren Holloway</p>
      <ul>
        <li>
          <svg viewBox="0 0 16 16" aria-hidden="true"><path d="M2 5c0-2 3-3 6-3s6 1 6 3v1h-3V5H5v1H2z M4 7h8l2 6H2z"/></svg>
          405-718-2954
        </li>
        <li>
          <svg viewBox="0 0 16 16" aria-hidden="true"><path d="M1 3h14v10H1z M2 4l6 5 6-5" stroke="#f3f3f3" stroke-width="1.2"/></svg>
          Help@tandrelyns.com
        </li>
        <li>
          <svg viewBox="0 0 16 16" aria-hidden="true"><circle cx="8" cy="8" r="7"/><path d="M1 8h14 M8 1v14 M3 4h10 M3 12h10" stroke="#f3f3f3" stroke-width="0.9" fill="none"/><ellipse cx="8" cy="8" rx="3" ry="7" stroke="#f3f3f3" stroke-width="0.9" fill="none"/></svg>
          www.tandrelyns.com
        </li>
      </ul>
      <p class="address" style="margin-bottom:0">4170 SW 38th Ave. okc, ok 73119</p>
    </div>

    <svg class="back-footer" viewBox="0 0 620 48" aria-hidden="true">
      <rect x="0" y="34" width="290" height="14" fill="var(--orange)"/>
      <path d="M286 48 L304 6 Q306 0 314 0 H620 V48 Z" fill="var(--navy)"/>
    </svg>
    <span class="tagline">We're here when you need us</span>
  </section>

</main>
</body>
</html>
```